KLR Values Puzzle Pieces

I want to use my logo (symbol only, not the words Marbel Vein Center) as the basis of the puzzle and incorporate our four values into the logo as four puzzle pieces. I want each puzzle piece to have one value on it and a line extending from the piece. At this point, I would like the bullet points of each value to be listed.
Here are the four values with the bullet points:
Cheese Movers
Are open to and embrace change, recognizing that it is a process, not a one-time event.
Are lifelong learners who continually use incremental improvements to enhance their knowledge and skills.
Possess grit, a combination of passion and perseverance, which allows them to overcome challenges and achieve their goals. Grit is the fuel to stay motivated and determined even when faced with obstacles or setbacks.
Are self-disciplined, working smart in thought and action by intentionally focusing on their goals.
Servant-Minded
Approaches work with humility, grace, and mercy, recognizing that serving others is a privilege.
Have a patient-centric approach, looking at the processes through the patient's eyes to ensure the best possible experience.
Educating patients with clarity and consistency, ensuring that they understand vein disease is a treatable but not curable condition.
The "Front Porch Rule" is a guiding principle that everyone is treated with respect, care, and compassion like our beloved family members.
We seek to provide vein care to all who need it.
Better Together
We emphasize the importance of having a team that rows in the same direction towards a common goal.
We have accountability and integrity by taking responsibility for our actions and their impact on others.
We are courageously real, speaking authentically to share thoughts and ideas while feeling valued for our unique perspectives.
We prioritize creating a supportive environment where team members feel they have the resources needed to succeed.
Balanced
We emphasize the importance of maintaining a work-life balance.
We are professional and take what we do seriously while still using laughter and fun to create a welcoming and friendly environment for patients and staff.
Valuable output is the greatest measure, not hours put in. Anyone can keep busy, but that does not equate to productivity.

```html
<!DOCTYPE html>
<html lang="en">
<head>
<meta charset="utf-8">
<title>KLR Values</title>
<link rel="stylesheet" href="https://fonts.googleapis.com/css2?family=Montserrat:wght@400;500;600&display=swap">
<style>
  :root {
    --stage: #000000;
    --navy: #0a1a8a;
    --navy-deep: #2333a0;
    --lavender: #e6e6f4;
    --green: #008a3e;
    --green-pale: #d9efe2;
    --slate: #6e808f;
    --slate-pale: #e8eaee;
    --ink: #10121a;
    --white: #ffffff;
  }
  * { margin: 0; padding: 0; box-sizing: border-box; }
  html, body { width: 1200px; height: 1200px; overflow: hidden; background: var(--stage); }
  .canvas { position: relative; width: 1200px; height: 1200px; font-family: "Montserrat", sans-serif; color: var(--ink); }
  .sheet { position: absolute; left: 84px; top: 201px; width: 1032px; height: 797px; overflow: hidden; }
  .quadrant { position: absolute; }
  .quadrant--change { left: 0; top: 0; width: 526px; height: 391px; background: radial-gradient(circle at 100% 100%, var(--lavender) 0%, #a9acdb 40%, var(--navy-deep) 100%); }
  .quadrant--service { left: 526px; top: 0; width: 506px; height: 391px; background: radial-gradient(circle at 0% 100%, var(--lavender) 0%, #a9acdb 40%, var(--navy-deep) 100%); }
  .quadrant--team { left: 0; top: 391px; width: 526px; height: 406px; background: radial-gradient(circle at 100% 0%, var(--green-pale) 0%, #8ccaa6 50%, var(--green) 100%); }
  .quadrant--balance { left: 526px; top: 391px; width: 506px; height: 406px; background: radial-gradient(circle at 0% 0%, var(--slate-pale) 0%, #b5bcc5 50%, var(--slate) 100%); }
  .connectors { position: absolute; left: 0; top: 0; width: 1200px; height: 1200px; }
  .values-text { position: absolute; width: 330px; font-size: 12.4px; line-height: 18.3px; letter-spacing: 0.15px; }
  .values-text p + p { margin-top: 8px; }
  .values-text--change { left: 131px; top: 302px; }
  .values-text--service { left: 746px; top: 302px; }
  .values-text--team { left: 131px; top: 673px; }
  .values-text--balance { left: 746px; top: 673px; }
  .hub { position: absolute; left: 471px; top: 471px; width: 256px; height: 256px; border-radius: 50%; background: var(--white); display: flex; align-items: center; justify-content: center; }
  .hub-name { font-size: 40px; font-weight: 600; color: var(--navy); letter-spacing: 2px; }
  .value-label { position: absolute; font-size: 14px; font-weight: 600; white-space: nowrap; }
  .value-label--change { left: 500px; top: 525px; color: var(--navy); }
  .value-label--service { left: 612px; top: 525px; color: var(--navy); }
  .value-label--team { left: 498px; top: 660px; color: var(--green); }
  .value-label--balance { left: 630px; top: 660px; color: #4f5f6d; }
</style>
</head>
<body>
<div class="canvas">
  <div class="sheet">
    <div class="quadrant quadrant--change"></div>
    <div class="quadrant quadrant--service"></div>
    <div class="quadrant quadrant--team"></div>
    <div class="quadrant quadrant--balance"></div>
  </div>

  <svg class="connectors" viewBox="0 0 1200 1200" aria-hidden="true">
    <g fill="none" stroke-width="2">
      <polyline points="142,263 492,263 492,520" stroke="#0a1a8a"/>
      <polyline points="1058,263 707,263 707,520" stroke="#0a1a8a"/>
      <polyline points="142,941 492,941 492,671" stroke="#0b8a42"/>
      <polyline points="1058,941 707,941 707,671" stroke="#6e808f"/>
    </g>
    <circle cx="142" cy="263" r="7.5" fill="#fff" stroke="#0a1a8a" stroke-width="4"/>
    <circle cx="1058" cy="263" r="7.5" fill="#fff" stroke="#0a1a8a" stroke-width="4"/>
    <circle cx="142" cy="941" r="7.5" fill="#fff" stroke="#0b8a42" stroke-width="4"/>
    <circle cx="1058" cy="941" r="6" fill="#fff"/>
  </svg>

  <div class="values-text values-text--change">
    <p>Are open to and embrace change, recognizing that it is a process, not a one-time event.</p>
    <p>Are lifelong learners who continually use incremental improvements to enhance their knowledge and skills.</p>
    <p>Possess grit, a combination of passion and perseverance, which allows them to overcome challenges and achieve their goals. Grit is the fuel to stay motivated and determined even when faced with obstacles or setbacks. Are self-disciplined, working smart in thought and action by intentionally focusing on their goals.</p>
  </div>

  <div class="values-text values-text--service">
    <p>Approaches work with humility, grace, and mercy, recognizing that serving others is a privilege.</p>
    <p>Have a patient-centric approach, looking at the processes through the patient's eyes to ensure the best possible experience.</p>
    <p>Educating patients with clarity and consistency, ensuring that they understand vein disease is a treatable but not curable condition.</p>
    <p>The "Front Porch Rule" is a guiding principle that everyone is treated with respect, care, and compassion like our beloved family members.</p>
    <p>We seek to provide vein care to all who need it.</p>
  </div>

  <div class="values-text values-text--team">
    <p>We emphasize the importance of having a team that rows in the same direction towards a common goal.</p>
    <p>We have accountability and integrity by taking responsibility for our actions and their impact on others.</p>
    <p>We are courageously real, speaking authentically to share thoughts and ideas while feeling valued for our unique perspectives.</p>
    <p>We prioritize creating a supportive environment where team members feel they have the resources needed to succeed.</p>
  </div>

  <div class="values-text values-text--balance">
    <p>We emphasize the importance of maintaining a work-life balance.</p>
    <p>We are professional and take what we do seriously while still using laughter and fun to create a welcoming and friendly environment for patients and staff.</p>
    <p>Valuable output is the greatest measure, not hours put in. Anyone can keep busy, but that does not equate to productivity.</p>
  </div>

  <div class="hub"><span class="hub-name">KLR</span></div>
  <span class="value-label value-label--change">Cheese Movers</span>
  <span class="value-label value-label--service">Servant-Minded</span>
  <span class="value-label value-label--team">Better Together</span>
  <span class="value-label value-label--balance">Balanced</span>
</div>
</body>
</html>
```